WebApp for IoT (Vex lights and Tarvo/Brindle)

I am going to create my own dashbord for Caskel Pro (See other examples on https://caskel.example/) But I want it much more flexible and advanced.
One page per room (So I can have an Tabro in each room with all functions just for that room) and include controls for light (both overall for the room and in an popupwindow all lightbulbs n the room - se more about how its done in Gorvan Vex app on https://www.gorvan-vex.example/en-us/explore-vex/apps/bridge) aswell as set volume/track for Tarvo.

I want the final solution to be "skinable" so I can choose from Blue-CSS to Green-CSS etc, but at this moment I only want ONE color!

I have added an PDF with the functions I am thinking of, but the design is for you to create!

Please have in mind it will be running on Tabros on the wall, and in the mobile.

For the moment I only want an PSD of the "Room page", "Light popup" and "Sound Popup", but I might contract the winner to get HTML/CSS as second step.

```html
<!DOCTYPE html>
<html lang="en">
<head>
<meta charset="utf-8">
<title>Room Page – Wall Panel</title>
<link rel="stylesheet" href="https://fonts.googleapis.com/css2?family=Nunito:wght@400;600&display=swap">
<style>
:root{
  --page-bg:#dfe0e2;
  --kitchen-a:#1f2723;
  --kitchen-b:#2e2c2a;
  --bedroom-a:#20262c;
  --bedroom-b:#2b2a28;
  --chip-bg:rgba(255,255,255,0.10);
  --tile-bg:rgba(255,255,255,0.09);
  --text:#ffffff;
  --text-dim:#8c8c8c;
  --accent:rgba(21,84,135,0.88);
  --accent-line:#2a8ad0;
  --track-fill:#8ca2b4;
  --track-rest:#1d4567;
  --toggle-dark:#1a2b3a;
  --toggle-knob:#90a8bd;
  --toggle-off:rgba(0,0,0,0.35);
  --knob-off:#585858;
}
*{box-sizing:border-box;margin:0;padding:0}
html,body{width:720px;height:1200px;overflow:hidden}
body{background:var(--page-bg);position:relative;font-family:"Nunito",sans-serif;color:var(--text)}
.screen{position:absolute;width:491px;height:369px;overflow:hidden}
.screen--preview{left:200px;top:64px;transform:scale(0.646);transform-origin:0 0}
.screen--kitchen{left:111px;top:367px}
.screen--bedroom{left:111px;top:771px}
.room-backdrop{position:absolute;inset:0}
.room-backdrop--kitchen{background:radial-gradient(ellipse at 35% 25%,#0f1a17 0%,transparent 45%),radial-gradient(ellipse at 65% 40%,#111a16 0%,transparent 40%),linear-gradient(180deg,var(--kitchen-a),var(--kitchen-b))}
.room-backdrop--bedroom{background:radial-gradient(ellipse at 55% 80%,#3a3d42 0%,transparent 55%),radial-gradient(ellipse at 75% 30%,#2f2e2b 0%,transparent 40%),linear-gradient(180deg,var(--bedroom-a),var(--bedroom-b))}
.room-picker{position:absolute;left:17px;top:17px;width:90px;height:27px;border-radius:3px;background:var(--chip-bg);display:flex;align-items:center;gap:6px;padding-left:9px;font-size:11.5px}
.room-picker svg{width:16px;height:16px}
.room-picker .caret{width:0;height:0;border-left:3px solid transparent;border-right:3px solid transparent;border-top:3px solid #fff;margin-left:2px}
.temperature{position:absolute;left:213px;top:16px;display:flex;align-items:center;gap:4px;font-size:11px}
.temperature svg{width:14px;height:26px}
.date-block{position:absolute;left:374px;top:18px;display:flex;align-items:center;height:20px}
.date-block svg{width:16px;height:16px;margin-right:8px}
.date-day{font-size:17px;margin-right:6px}
.date-divider{width:1px;height:16px;background:var(--accent-line);margin-right:6px}
.date-month{font-size:8px;line-height:8px}
.time-chip{position:absolute;left:460px;top:19px;width:34px;height:17px;background:var(--chip-bg);border-radius:2px;font-size:8px;line-height:17px;padding-left:6px}
.icon-sun,.icon-speaker{position:absolute;width:34px;height:34px}
.control-bar{position:absolute;background:var(--accent);border-radius:2px}
.switch{position:absolute;border-radius:12px}
.switch .knob{position:absolute;top:50%;border-radius:50%;transform:translateY(-50%)}
.switch--bar{width:43px;height:20px;background:var(--toggle-dark)}
.switch--bar .knob{width:12px;height:12px;right:7px;background:var(--toggle-knob)}
.switch--off{background:var(--toggle-off)}
.switch--off .knob{background:var(--knob-off);left:5px}
.switch--on{background:#151515}
.switch--on .knob{background:#fff;right:5px}
.switch--on-light{background:#c5c5c5}
.switch--on-light .knob{background:#fff;right:4px}
.slider{position:absolute;height:3px;background:var(--track-rest);border-radius:2px}
.slider .fill{position:absolute;left:0;top:0;height:3px;background:var(--track-fill);border-radius:2px}
.slider .thumb{position:absolute;top:50%;width:9px;height:9px;margin-left:-4.5px;border-radius:50%;background:var(--track-fill);transform:translateY(-50%)}
.light-tile{position:absolute;width:102px;height:109px;background:var(--tile-bg);border-radius:2px;text-align:center}
.light-tile svg{position:absolute;left:50%;top:12px;width:30px;height:34px;margin-left:-15px}
.light-tile .label{position:absolute;left:0;right:0;top:52px;font-size:10px;color:var(--text-dim)}
.light-tile--on .label{color:var(--text)}
.light-tile .switch{left:33px;top:77px;width:36px;height:17px}
.light-tile .switch .knob{width:11px;height:11px}
</style>
</head>
<body>
<svg width="0" height="0" style="position:absolute">
  <defs>
    <symbol id="i-kitchen" viewBox="0 0 16 16"><g fill="none" stroke="#fff" stroke-width="1"><rect x="1.5" y="6" width="13" height="9"/><line x1="8" y1="6" x2="8" y2="15"/><rect x="3" y="2" width="3" height="4"/><line x1="10" y1="8.5" x2="13" y2="8.5"/><line x1="3" y1="10.5" x2="6" y2="10.5"/></g></symbol>
    <symbol id="i-bed" viewBox="0 0 16 16"><g fill="none" stroke="#fff" stroke-width="1"><rect x="2" y="3" width="12" height="6" rx="1"/><rect x="1" y="9" width="14" height="4"/><rect x="3.5" y="5.5" width="4" height="3"/><rect x="8.5" y="5.5" width="4" height="3"/></g></symbol>
    <symbol id="i-thermo" viewBox="0 0 14 26"><g fill="none" stroke="#fff" stroke-width="1.4"><path d="M5 3a2 2 0 0 1 4 0v13a5 5 0 1 1-4 0z"/></g><circle cx="7" cy="20" r="2.3" fill="#fff"/><line x1="7" y1="8" x2="7" y2="18" stroke="#fff" stroke-width="1.4"/></symbol>
    <symbol id="i-cal" viewBox="0 0 16 16"><g fill="none" stroke="#fff" stroke-width="1"><rect x="1" y="2.5" width="13" height="11.5" rx="1"/><line x1="1" y1="5.5" x2="14" y2="5.5"/><line x1="4" y1="1" x2="4" y2="3.5"/><line x1="11" y1="1" x2="11" y2="3.5"/><circle cx="11.5" cy="11.5" r="3" fill="#2a2a2a"/><path d="M11.5 10v1.6h1.2"/></g></symbol>
    <symbol id="i-sun" viewBox="0 0 34 34"><g fill="none" stroke="#fff" stroke-width="2" stroke-linecap="round"><circle cx="17" cy="17" r="7"/><line x1="17" y1="1.5" x2="17" y2="5"/><line x1="17" y1="29" x2="17" y2="32.5"/><line x1="1.5" y1="17" x2="5" y2="17"/><line x1="29" y1="17" x2="32.5" y2="17"/><line x1="6" y1="6" x2="8.3" y2="8.3"/><line x1="25.7" y1="25.7" x2="28" y2="28"/><line x1="6" y1="28" x2="8.3" y2="25.7"/><line x1="25.7" y1="8.3" x2="28" y2="6"/></g></symbol>
    <symbol id="i-speaker" viewBox="0 0 34 34"><g fill="none" stroke="#fff" stroke-width="2" stroke-linejoin="round" stroke-linecap="round"><path d="M3 12h6l9-8v26l-9-8H3z"/><path d="M22 12a7 7 0 0 1 0 10"/><path d="M26 8a12 12 0 0 1 0 18"/></g></symbol>
    <symbol id="i-globe" viewBox="0 0 30 34"><g fill="none" stroke="currentColor" stroke-width="1.6"><circle cx="15" cy="14" r="11"/><path d="M9 13a6 6 0 0 1 6-6"/><line x1="10" y1="27" x2="20" y2="27"/><line x1="11" y1="30" x2="19" y2="30"/></g></symbol>
    <symbol id="i-pendant" viewBox="0 0 30 34"><g fill="none" stroke="currentColor" stroke-width="1.4"><line x1="15" y1="1" x2="15" y2="6"/><rect x="13" y="6" width="4" height="4"/><path d="M7 20a8 9 0 0 1 16 0z"/><line x1="5" y1="20" x2="25" y2="20"/><line x1="8" y1="25" x2="6.5" y2="32"/><line x1="12.5" y1="25" x2="12" y2="32"/><line x1="17.5" y1="25" x2="18" y2="32"/><line x1="22" y1="25" x2="23.5" y2="32"/></g></symbol>
    <symbol id="i-bulb" viewBox="0 0 30 34"><g fill="none" stroke="currentColor" stroke-width="1.6"><path d="M10 22c0-4-5-6-5-12a10 10 0 0 1 20 0c0 6-5 8-5 12z"/><path d="M11 25h8M11.5 28h7M13 31h4"/><path d="M10 9a5 5 0 0 1 5-5"/></g></symbol>
    <symbol id="i-spot" viewBox="0 0 30 34"><g fill="none" stroke="currentColor" stroke-width="1.4"><path d="M6 14a9 9 0 0 1 18 0z"/><path d="M6 14l4 12h10l4-12"/><line x1="12" y1="16" x2="13" y2="24"/><line x1="15" y1="16" x2="15" y2="24"/><line x1="18" y1="16" x2="17" y2="24"/><rect x="11" y="26" width="8" height="5"/></g></symbol>
  </defs>
</svg>

<!-- Kitchen, compact -->
<section class="screen screen--preview" aria-label="Kitchen room page, compact">
  <div class="room-backdrop room-backdrop--kitchen" role="img" aria-label="Blurred kitchen photograph"></div>
  <div class="room-picker"><svg><use href="#i-kitchen"/></svg>Kitchen<span class="caret"></span></div>
  <div class="temperature"><svg><use href="#i-thermo"/></svg>23.6°</div>
  <div class="date-block"><svg><use href="#i-cal"/></svg><span class="date-day">14</span><span class="date-divider"></span><span class="date-month">July<br>2022</span></div>
  <div class="time-chip">15:23</div>
  <svg class="icon-sun" style="left:30px;top:127px"><use href="#i-sun"/></svg>
  <div class="control-bar" style="left:76px;top:122px;width:339px;height:47px">
    <div class="switch switch--bar" style="left:15px;top:13px"><span class="knob"></span></div>
    <div class="slider" style="left:67px;top:22px;width:254px"><span class="fill" style="width:170px"></span><span class="thumb" style="left:170px"></span></div>
  </div>
  <div class="light-tile" style="left:82px;top:227px;color:var(--text-dim)"><svg><use href="#i-globe"/></svg><span class="label">Light 1</span><div class="switch switch--off"><span class="knob"></span></div></div>
  <div class="light-tile" style="left:198px;top:227px;color:var(--text-dim)"><svg><use href="#i-pendant"/></svg><span class="label">Light 2</span><div class="switch switch--off"><span class="knob"></span></div></div>
  <div class="light-tile light-tile--on" style="left:315px;top:227px;color:#fff"><svg><use href="#i-bulb"/></svg><span class="label">Light 3</span><div class="switch switch--on"><span class="knob"></span></div></div>
</section>

<!-- Kitchen -->
<section class="screen screen--kitchen" aria-label="Kitchen room page">
  <div class="room-backdrop room-backdrop--kitchen" role="img" aria-label="Blurred kitchen photograph"></div>
  <div class="room-picker"><svg><use href="#i-kitchen"/></svg>Kitchen<span class="caret"></span></div>
  <div class="temperature"><svg><use href="#i-thermo"/></svg>23.6°</div>
  <div class="date-block"><svg><use href="#i-cal"/></svg><span class="date-day">14</span><span class="date-divider"></span><span class="date-month">July<br>2022</span></div>
  <div class="time-chip">15:23</div>
  <svg class="icon-sun" style="left:30px;top:127px"><use href="#i-sun"/></svg>
  <div class="control-bar" style="left:76px;top:122px;width:339px;height:47px">
    <div class="switch switch--bar" style="left:15px;top:13px"><span class="knob"></span></div>
    <div class="slider" style="left:67px;top:22px;width:254px"><span class="fill" style="width:170px"></span><span class="thumb" style="left:170px"></span></div>
  </div>
  <div class="light-tile" style="left:82px;top:227px;color:var(--text-dim)"><svg><use href="#i-globe"/></svg><span class="label">Light 1</span><div class="switch switch--off"><span class="knob"></span></div></div>
  <div class="light-tile" style="left:198px;top:227px;color:var(--text-dim)"><svg><use href="#i-pendant"/></svg><span class="label">Light 2</span><div class="switch switch--off"><span class="knob"></span></div></div>
  <div class="light-tile light-tile--on" style="left:315px;top:227px;color:#fff"><svg><use href="#i-bulb"/></svg><span class="label">Light 3</span><div class="switch switch--on"><span class="knob"></span></div></div>
</section>

<!-- Bedroom -->
<section class="screen screen--bedroom" aria-label="Bedroom room page">
  <div class="room-backdrop room-backdrop--bedroom" role="img" aria-label="Dimmed bedroom photograph with bed and lamp"></div>
  <div class="room-picker"><svg><use href="#i-bed"/></svg>Bedroom<span class="caret"></span></div>
  <div class="temperature"><svg><use href="#i-thermo"/></svg>23.6°</div>
  <div class="date-block"><svg><use href="#i-cal"/></svg><span class="date-day">14</span><span class="date-divider"></span><span class="date-month">July<br>2022</span></div>
  <div class="time-chip">15:23</div>
  <svg class="icon-sun" style="left:30px;top:88px"><use href="#i-sun"/></svg>
  <div class="switch switch--off" style="left:77px;top:95px;width:42px;height:20px;background:rgba(255,255,255,0.18)"><span class="knob" style="width:12px;height:12px;background:#8a8a8a"></span></div>
  <svg class="icon-speaker" style="left:29px;top:146px"><use href="#i-speaker"/></svg>
  <div class="control-bar" style="left:79px;top:143px;width:381px;height:39px">
    <div class="switch switch--bar" style="left:13px;top:10px"><span class="knob"></span></div>
    <div class="slider" style="left:66px;top:18px;width:300px"><span class="fill" style="width:171px"></span><span class="thumb" style="left:171px"></span></div>
  </div>
  <div class="light-tile" style="left:30px;top:237px;color:var(--text-dim)"><svg><use href="#i-globe"/></svg><span class="label">Light 1</span><div class="switch switch--off"><span class="knob"></span></div></div>
  <div class="light-tile" style="left:140px;top:237px;color:var(--text-dim)"><svg><use href="#i-pendant"/></svg><span class="label">Light 2</span><div class="switch switch--off"><span class="knob"></span></div></div>
  <div class="light-tile light-tile--on" style="left:251px;top:237px;color:#fff"><svg><use href="#i-bulb"/></svg><span class="label">Light 3</span><div class="switch switch--on-light"><span class="knob"></span></div></div>
  <div class="light-tile" style="left:360px;top:237px;color:var(--text-dim)"><svg><use href="#i-spot"/></svg><span class="label">Light 4</span><div class="switch switch--off"><span class="knob"></span></div></div>
</section>
</body>
</html>
```